Signs to Go on the Side of Shipping Containers

We are a startup in North Alabama that will lease/sale shipping containers as Portable Storage options for business/construction sites. We need signs that will be mass produced and be mounted on every side of the container for advertising/visibility.
We need multiple sizes depending on the side the sign will be on/ the size of the container it is being mounted on.
Website: www.ridgelinebinworks.com

MUST BE SIMPLE AND EASY TO READ. Not to Busy. See example in
Updates

One designer is asking me to extend deadline. This is my first design project so not sure why they want me to do this but figured I would.

Target Market(s)

Business owners/Construction Companies/Individuals Moving

Industry/Entity Type

Portable Storage

Colors
0054AA
0677BA
7BADD7
CADEEF
E8F1F8

Requirements
Must have
• Company Name(Ridgeline Bin Works)/Phone Number (256-555-0147)/Website (www.ridgelinebinworks.com
Nice to have
• Play on the container shapes/pattern.

```html
<!DOCTYPE html>
<html lang="en">
<head>
<meta charset="utf-8">
<title>Ridgeline Bin Works – Container Sign</title>
<link rel="stylesheet" href="https://fonts.googleapis.com/css2?family=Montserrat:wght@700;800&family=Oswald:wght@700&display=swap">
<style>
  :root {
    --brand-blue: #0677BA;
    --deep-blue: #0054AA;
    --mid-blue: #7BADD7;
    --ink: #111111;
    --sign-white: #FFFFFF;
    --backdrop: #E6E6E6;
  }
  html, body {
    margin: 0;
    padding: 0;
    width: 1200px;
    height: 1200px;
    overflow: hidden;
    background: var(--backdrop);
  }
  .sign {
    position: absolute;
    left: 40px;
    top: 320px;
    width: 1120px;
    height: 560px;
    background: var(--sign-white);
  }
  .container-art {
    position: absolute;
    left: 82px;
    top: 50px;
    width: 270px;
    height: 248px;
  }
  .brand {
    position: absolute;
    left: 382px;
    top: 44px;
    width: 660px;
    text-align: center;
  }
  .brand-name {
    margin: 0;
    font-family: "Oswald", sans-serif;
    font-weight: 700;
    font-size: 94px;
    line-height: 0.98;
    color: var(--brand-blue);
    letter-spacing: 1px;
  }
  .tagline {
    margin: 14px 0 0;
    font-family: "Montserrat", sans-serif;
    font-weight: 800;
    font-size: 34px;
    letter-spacing: 9px;
    color: var(--ink);
  }
  .phone {
    position: absolute;
    left: 0;
    right: 0;
    top: 340px;
    margin: 0;
    text-align: center;
    font-family: "Montserrat", sans-serif;
    font-weight: 800;
    font-size: 112px;
    line-height: 1;
    color: var(--ink);
  }
  .website {
    position: absolute;
    left: 0;
    right: 0;
    top: 470px;
    margin: 0;
    text-align: center;
    font-family: "Montserrat", sans-serif;
    font-weight: 700;
    font-size: 47px;
    line-height: 1;
    letter-spacing: 2px;
    color: var(--ink);
  }
</style>
</head>
<body>
  <main class="sign">
    <svg class="container-art" viewBox="0 0 270 248" role="img" aria-label="Illustration of a blue shipping container seen at an angle">
      <defs>
        <linearGradient id="containerTone" x1="0" y1="0" x2="1" y2="1">
          <stop offset="0" stop-color="#0677BA"/>
          <stop offset="1" stop-color="#0054AA"/>
        </linearGradient>
      </defs>
      <rect x="0" y="0" width="270" height="248" fill="url(#containerTone)"/>
    </svg>

    <header class="brand">
      <h1 class="brand-name">RIDGELINE<br>BIN WORKS</h1>
      <p class="tagline">SALES &amp; RENTALS</p>
    </header>

    <p class="phone">256-555-0147</p>
    <p class="website">www.ridgelinebinworks.com</p>
  </main>
</body>
</html>
```